San Francisco Hotel - Fun Brochure Design

Hey!
I need a brochure that reflects my hotel's (Harlow's Motor Lodge) mid century modern feel while taking into account our excellent location in the Castro of San Francisco. I would like a fun brochure that is also sleek - on a rack of hotel brochures, I want ours to stand out, just like we do! Our building colors are quite bright - pinkish, blue and yellow - and are currently closely associated with us. Guests stay with us over and over again because of our wonderful location in the Castro (and very close to ZARN), our free parking (we're a motor lodge!), our free wireless internet and our reasonable rates. The final design should incorporate these things. In the coming year we will be going though renovations which will change our look (inside and out) and we will need completely new branding at that time as well.
LGTBQ, International travelers, 50+ year old couples
Wireless Internet

```html
<!DOCTYPE html>
<html lang="en">
<head>
<meta charset="utf-8">
<title>Harlow's Motor Lodge – Brochure</title>
<link href="https://fonts.googleapis.com/css2?family=Arimo:wght@400;700&family=Dancing+Script:wght@500&display=swap" rel="stylesheet">
<style>
  :root {
    --red: #e21c4b;
    --blue: #1f4f9f;
    --ink-blue: #2a4c9c;
    --check-red: #d7263d;
    --yellow: #fbd26c;
    --orange: #f2935a;
    --map-border: #f6c160;
    --ink: #1c1c1c;
  }
  * { margin: 0; padding: 0; box-sizing: border-box; }
  html, body { width: 1200px; height: 927px; overflow: hidden; background: #fff; }
  .brochure { position: relative; width: 1200px; height: 927px; font-family: "Arimo", Arial, sans-serif; background: #fff; }

  .band-top { position: absolute; left: 0; top: 0; width: 800px; height: 73px; background: var(--red); }
  .band-bottom { position: absolute; left: 0; top: 868px; width: 800px; height: 59px; background: var(--blue); }

  .amenities { position: absolute; left: 24px; top: 100px; width: 380px; }
  .amenities h2 { font-family: "Dancing Script", cursive; font-weight: 500; font-size: 36px; color: var(--ink-blue); margin-left: 88px; line-height: 48px; }
  .amenities ul { list-style: none; margin-top: 6px; }
  .amenities li { display: flex; align-items: center; height: 45.5px; font-size: 15.5px; color: var(--ink); }
  .amenities svg { width: 26px; height: 24px; margin-right: 10px; flex: none; }

  .wordmark { font-family: "Arimo", Arial, sans-serif; font-weight: 700; color: var(--blue); display: flex; align-items: center; gap: 10px; }
  .wordmark .dot { width: 18px; height: 18px; border-radius: 50%; background: var(--yellow); flex: none; }
  .wordmark-mid { position: absolute; left: 462px; top: 118px; width: 280px; justify-content: center; font-size: 27px; }
  .wordmark-side { position: absolute; left: 830px; top: 722px; width: 340px; justify-content: center; font-size: 32px; }

  .contact-mid { position: absolute; left: 400px; top: 276px; width: 400px; text-align: center; color: var(--ink-blue); font-weight: 700; font-size: 19px; line-height: 27.5px; }

  .map { position: absolute; left: 482px; top: 435px; width: 239px; height: 235px; border: 4px solid var(--map-border); background: #e8e4dc; }

  .transit-note { position: absolute; left: 444px; top: 732px; width: 316px; color: var(--check-red); font-weight: 700; font-size: 16.5px; line-height: 23.5px; text-align: justify; }

  .cover { position: absolute; left: 800px; top: 0; width: 400px; height: 927px; background: linear-gradient(180deg, var(--yellow) 35%, var(--orange) 100%); }
  .cover-photo { position: absolute; left: 0; top: 0; width: 400px; height: 270px; background: linear-gradient(180deg, #7fb2e0 0%, #a9c9e6 40%, #d9a67a 70%, #8c7a5a 100%); }
  .cover-title { position: absolute; left: 0; top: 270px; width: 400px; height: 95px; background: var(--red); color: #fff; font-family: "Dancing Script", cursive; font-weight: 500; font-size: 37px; display: flex; align-items: center; justify-content: center; }
  .cover-city { position: absolute; left: 0; top: 386px; width: 400px; text-align: center; color: var(--ink-blue); font-weight: 700; font-size: 25px; }
  .contact-side { position: absolute; left: 0; top: 824px; width: 400px; text-align: center; color: var(--ink); font-weight: 700; font-size: 15.5px; line-height: 23.5px; }
</style>
</head>
<body>
<div class="brochure">
  <div class="band-top"></div>
  <div class="band-bottom"></div>

  <section class="amenities">
    <h2>Amenities</h2>
    <ul>
      <li><svg viewBox="0 0 26 24"><rect x="1" y="5" width="17" height="17" fill="none" stroke="#555" stroke-width="1.5"/><path d="M5 13 l5 6 L24 2" fill="none" stroke="var(--check-red)" stroke-width="3"/></svg>Free Wireless Internet in Every Room</li>
      <li><svg viewBox="0 0 26 24"><rect x="1" y="5" width="17" height="17" fill="none" stroke="#555" stroke-width="1.5"/><path d="M5 13 l5 6 L24 2" fill="none" stroke="var(--check-red)" stroke-width="3"/></svg>Free Parking</li>
      <li><svg viewBox="0 0 26 24"><rect x="1" y="5" width="17" height="17" fill="none" stroke="#555" stroke-width="1.5"/><path d="M5 13 l5 6 L24 2" fill="none" stroke="var(--check-red)" stroke-width="3"/></svg>100% Non-Smoking</li>
      <li><svg viewBox="0 0 26 24"><rect x="1" y="5" width="17" height="17" fill="none" stroke="#555" stroke-width="1.5"/><path d="M5 13 l5 6 L24 2" fill="none" stroke="var(--check-red)" stroke-width="3"/></svg>Safe Deposit Box at Front Desk</li>
      <li><svg viewBox="0 0 26 24"><rect x="1" y="5" width="17" height="17" fill="none" stroke="#555" stroke-width="1.5"/><path d="M5 13 l5 6 L24 2" fill="none" stroke="var(--check-red)" stroke-width="3"/></svg>Sun Deck</li>
      <li><svg viewBox="0 0 26 24"><rect x="1" y="5" width="17" height="17" fill="none" stroke="#555" stroke-width="1.5"/><path d="M5 13 l5 6 L24 2" fill="none" stroke="var(--check-red)" stroke-width="3"/></svg>Two Rooms with Fireplaces</li>
      <li><svg viewBox="0 0 26 24"><rect x="1" y="5" width="17" height="17" fill="none" stroke="#555" stroke-width="1.5"/><path d="M5 13 l5 6 L24 2" fill="none" stroke="var(--check-red)" stroke-width="3"/></svg>24 Hour Front Desk</li>
      <li><svg viewBox="0 0 26 24"><rect x="1" y="5" width="17" height="17" fill="none" stroke="#555" stroke-width="1.5"/><path d="M5 13 l5 6 L24 2" fill="none" stroke="var(--check-red)" stroke-width="3"/></svg>Air Conditioned King Deluxe Rooms</li>
      <li><svg viewBox="0 0 26 24"><rect x="1" y="5" width="17" height="17" fill="none" stroke="#555" stroke-width="1.5"/><path d="M5 13 l5 6 L24 2" fill="none" stroke="var(--check-red)" stroke-width="3"/></svg>Hair Dryers Available</li>
      <li><svg viewBox="0 0 26 24"><rect x="1" y="5" width="17" height="17" fill="none" stroke="#555" stroke-width="1.5"/><path d="M5 13 l5 6 L24 2" fill="none" stroke="var(--check-red)" stroke-width="3"/></svg>Coffee Makers</li>
      <li><svg viewBox="0 0 26 24"><rect x="1" y="5" width="17" height="17" fill="none" stroke="#555" stroke-width="1.5"/><path d="M5 13 l5 6 L24 2" fill="none" stroke="var(--check-red)" stroke-width="3"/></svg>Guest Laundry Room</li>
      <li><svg viewBox="0 0 26 24"><rect x="1" y="5" width="17" height="17" fill="none" stroke="#555" stroke-width="1.5"/><path d="M5 13 l5 6 L24 2" fill="none" stroke="var(--check-red)" stroke-width="3"/></svg>Phones with Voicemail</li>
      <li><svg viewBox="0 0 26 24"><rect x="1" y="5" width="17" height="17" fill="none" stroke="#555" stroke-width="1.5"/><path d="M5 13 l5 6 L24 2" fill="none" stroke="var(--check-red)" stroke-width="3"/></svg>Flat Screen TVs in All Rooms with King Beds</li>
      <li><svg viewBox="0 0 26 24"><rect x="1" y="5" width="17" height="17" fill="none" stroke="#555" stroke-width="1.5"/><path d="M5 13 l5 6 L24 2" fill="none" stroke="var(--check-red)" stroke-width="3"/></svg>Refrigerators</li>
      <li><svg viewBox="0 0 26 24"><rect x="1" y="5" width="17" height="17" fill="none" stroke="#555" stroke-width="1.5"/><path d="M5 13 l5 6 L24 2" fill="none" stroke="var(--check-red)" stroke-width="3"/></svg>Private Baths in Each Room</li>
    </ul>
  </section>

  <div class="wordmark wordmark-mid"><span>Harlow's Motor Lodge</span><span class="dot"></span></div>

  <div class="contact-mid">
    <p>1480 Alder Street, San Francisco, CA</p>
    <p>(415) 555-0147</p>
    <p>info@HarlowsMotorLodge.com</p>
  </div>

  <div class="map" role="img" aria-label="Street map of the neighbourhood with the lodge location marked"></div>

  <p class="transit-note">Public transportation is conveniently located just steps away from our front door.</p>

  <aside class="cover">
    <div class="cover-photo" role="img" aria-label="Photo of the motor lodge building with palm trees under a blue sky"></div>
    <h1 class="cover-title">Harlow's Motor Lodge</h1>
    <p class="cover-city">San Francisco, CA</p>
    <div class="wordmark wordmark-side"><span>Harlow's Motor Lodge</span><span class="dot"></span></div>
    <div class="contact-side">
      <p>1480 Alder Street, San Francisco, CA</p>
      <p>(415) 555-0147</p>
      <p>info@HarlowsMotorLodge.com</p>
    </div>
  </aside>
</div>
</body>
</html>
```